Brellin Trade Partners - we are Asian sourcing agents

We are sourcing agents based in the USA and we act as sourcing agents for clients in throughout the world. We focus primarily on custom sewn goods. So basically companies who do not have the in-house expertise to do it themselves, come to us and have us find suitable factories in Asia to do the production. We are middlemen. We find the factories...quote the project...manage the quality control and then deliver the goods directly to our customer's door. We pride ourselves in making the communication very easy and precise.

Current page is www.brellintrade.example

I am not happy w/ the overall look. The spacing...the photos, the fonts...the design elements...the pictures. I want a cool, crisp design that conveys professionalism and clearly depicts/explains what we do.

Requirements
Must have
• use my logo....I like it...it was designed by someone on this website.
Nice to have
• a video/animation of the entire process would be wonderful. Showing initial contact with our office in the USA...then to my correspondence with my offices in Taiwan and in Hong Kong...and then back and fort w/ the customer.....and then between my people in Hong Kong/Taiwan with the local factories......and then a quote is generated and sent to my client......to samples being made and sent for approval.....to a PO being generated......to final samples being sent.....to the order being shipped and delivered to the clients warehouse. I was thinking of an animation showing arrows and text showing the back and forth communication and explaining how the process flows.

```html
<!DOCTYPE html>
<html lang="en">
<head>
<meta charset="utf-8">
<title>Brellin Trade Partners</title>
<link rel="stylesheet" href="https://fonts.googleapis.com/css2?family=Raleway:wght@200;300&family=PT+Sans:wght@400&display=swap">
<style>
:root{
  --olive:#74910f;
  --navy:#13205e;
  --ink:#000;
  --white:#fff;
}
*{margin:0;padding:0;box-sizing:border-box}
html,body{width:967px;height:1200px;overflow:hidden;background:var(--white);font-family:"PT Sans",Tahoma,sans-serif;color:var(--ink)}
.site-header{position:relative;height:95px}
.brand{position:absolute;left:34px;top:28px;display:flex;align-items:center;gap:8px;font-size:22px;color:var(--navy);font-weight:400;letter-spacing:.5px}
.brand-mark{width:14px;height:14px;background:var(--olive)}
.main-nav{position:absolute;left:632px;top:37px;display:flex;gap:17px;font-size:12px}
.main-nav a{color:var(--ink);text-decoration:none}
.hero{height:267px;background:var(--olive);color:var(--white);text-align:center;font-family:"Raleway",sans-serif;font-weight:200}
.hero h1{font-weight:200;font-size:46px;padding-top:92px;line-height:1}
.hero p{font-weight:300;font-size:24px;margin-top:14px}
.content{padding:49px 0 0 120px}
.tag-dark{display:inline-block;width:310px;height:41px;background:var(--ink);color:var(--white);font-size:18px;line-height:41px;padding-left:30px}
.intro{width:680px;margin:38px 0 0 29px;font-size:11.6px;line-height:19.3px}
.tag-olive{width:728px;height:41px;background:var(--olive);color:var(--white);font-size:18px;line-height:41px;padding-left:30px;margin-top:67px}
.products{display:grid;grid-template-columns:repeat(3,205px);column-gap:57px;row-gap:60px;margin-top:52px}
.product{height:160px}
.site-footer{position:absolute;left:0;top:1155px;width:967px;height:45px;background:var(--ink)}
</style>
</head>
<body>
<header class="site-header">
  <div class="brand"><span class="brand-mark"></span>Brellin Trade Partners</div>
  <nav class="main-nav"><a href="#">HOME</a><a href="#">ABOUT US</a><a href="#">PRODUCTS</a><a href="#">CONTACT US</a></nav>
</header>
<section class="hero">
  <h1>Asian Outsourcing Made Easy!</h1>
  <p>Custom Sewn Goods Made to Your Specifications</p>
</section>
<main class="content">
  <h2 class="tag-dark" style="font-weight:400">Sourcing custom goods in China</h2>
  <p class="intro">We outsource sewing services direct from China. Our long-established and extensive network of offshore factory-partners provides our clients with access to a wide variety of contract sewing expertise from Chinese manufacturers. Clients only need to communicate with our US agents, but will have the benefits of the cost savings &amp; quality workmanship from offshore outsourcing from Asia.</p>
  <h2 class="tag-olive" style="font-weight:400">Latest Products Specially Designed for you</h2>
  <div class="products">
    <div class="product" role="img" aria-label="Pair of white and black ski gloves" style="background:linear-gradient(#e6e6e6,#cfcfcf)"></div>
    <div class="product" role="img" aria-label="Black messenger bag with grey and red stripes" style="background:linear-gradient(90deg,#2a2a2a,#6a6a6a 45%,#c0262a 55%,#2a2a2a)"></div>
    <div class="product" role="img" aria-label="Navy and silver motorcycle cover" style="background:linear-gradient(#1f2f7a,#bdbdbd)"></div>
    <div class="product" role="img" aria-label="Row of colourful phone cases" style="background:linear-gradient(90deg,#222,#2b3ab0,#6a2aa0,#c0309a,#d0202a,#e0a020)"></div>
    <div class="product" role="img" aria-label="Red, white and black golf bags" style="background:linear-gradient(90deg,#333,#c02a2a,#eee,#c02a2a,#333)"></div>
    <div class="product" role="img" aria-label="Black crocodile-textured cosmetic case" style="background:linear-gradient(#3a3a3a,#111)"></div>
  </div>
</main>
<footer class="site-footer"></footer>
</body>
</html>
```